I have a website called Nexa Holdings (nexaholdings.com) that I would like to have redesigned. Most of the content is already created, but I need a new design. You can also see my other website at corbelestates.com. I am open to a new logo or modifying the current logo if you have a good idea. Please feel free to use other images for the home page (and maybe some other locations) if you feel they provide a better look and feel to the website. I prefer a modern look.

Important: You do not have to use the images I've provided for the home page. Feel free to find your own stock photos. You don't have to pay for them unless I select your design.

1) Please use wix.com to make your changes so that I can edit it later.
2) I will need all the graphics files to be saved so I can dowload it for later.
3) I will be adding more content to the site later.
4) This site will likely be transferred over to corbelestates.com so if you make a logo please make one for Nexa Holdings and one for Corbel Estates.
5) You can use other images that you feel would help the look and feel of the website.

Real Estate

Coded - Design and coding required

5+ page

```html
<!DOCTYPE html>
<html lang="en">
<head>
<meta charset="UTF-8">
<title>Nexa Holdings</title>
<link href="https://fonts.googleapis.com/css2?family=Montserrat:wght@400;700&family=Roboto:wght@400&display=swap" rel="stylesheet">
<style>
  :root {
    --navy-deep: #1b1c48;
    --navy-mid: #2c3390;
    --sky-blue: #3440a8;
    --lavender: #8c84a8;
    --warm-glow: #c9b59a;
    --olive: #6e6d3a;
    --moss: #3e4128;
    --stone: #6d6a8c;
    --white: #ffffff;
    --rule: rgba(255, 255, 255, 0.85);
  }
  * { margin: 0; padding: 0; box-sizing: border-box; }
  html, body {
    width: 1200px;
    height: 779px;
    overflow: hidden;
    background: var(--navy-deep);
  }
  .hero {
    position: relative;
    width: 1200px;
    height: 779px;
    overflow: hidden;
    color: var(--white);
  }
  .hero-photo {
    position: absolute;
    inset: 0;
    background:
      radial-gradient(ellipse 14% 18% at 15% 34%, rgba(201, 181, 154, 0.75), transparent 100%),
      radial-gradient(ellipse 30% 40% at 14% 45%, rgba(140, 132, 168, 0.85), transparent 100%),
      radial-gradient(ellipse 26% 55% at 88% 48%, rgba(110, 109, 58, 0.9), transparent 100%),
      radial-gradient(ellipse 20% 40% at 97% 80%, rgba(62, 65, 40, 0.9), transparent 100%),
      radial-gradient(ellipse 30% 35% at 53% 16%, rgba(52, 64, 168, 0.95), transparent 100%),
      radial-gradient(ellipse 22% 28% at 66% 82%, rgba(109, 106, 140, 0.8), transparent 100%),
      radial-gradient(ellipse 30% 30% at 22% 88%, rgba(27, 28, 72, 0.9), transparent 100%),
      linear-gradient(100deg, #5c5880 0%, #4a4c8a 35%, var(--navy-mid) 52%, #4c4f5e 70%, var(--moss) 100%);
  }
  .hero-tint {
    position: absolute;
    inset: 0;
    background: linear-gradient(180deg, rgba(30, 32, 110, 0.25) 0%, rgba(28, 28, 80, 0.3) 100%);
  }
  .site-header {
    position: absolute;
    top: 0;
    left: 0;
    width: 1200px;
    height: 95px;
    border-bottom: 1px solid var(--rule);
  }
  .brand {
    position: absolute;
    left: 64px;
    top: 36px;
    display: flex;
    align-items: center;
    gap: 10px;
    font-family: 'Montserrat', sans-serif;
    font-weight: 700;
    font-size: 18px;
    color: var(--white);
    text-decoration: none;
  }
  .brand-mark {
    width: 18px;
    height: 18px;
    background: var(--white);
  }
  .main-nav a {
    position: absolute;
    top: 38px;
    font-family: 'Montserrat', sans-serif;
    font-weight: 400;
    font-size: 16px;
    color: var(--white);
    text-decoration: none;
    letter-spacing: 0.3px;
  }
  .nav-home { left: 472px; }
  .nav-about { left: 617px; }
  .nav-strategy { left: 760px; }
  .nav-project { left: 921px; }
  .nav-contact { left: 1073px; }
  .hero-content {
    position: absolute;
    left: 0;
    top: 291px;
    width: 1200px;
    text-align: center;
  }
  .hero-title {
    font-family: 'Montserrat', sans-serif;
    font-weight: 700;
    font-size: 38px;
    line-height: 57px;
    letter-spacing: 0.2px;
    text-transform: uppercase;
  }
  .hero-tagline {
    margin-top: 20px;
    font-family: 'Roboto', sans-serif;
    font-weight: 400;
    font-size: 25px;
    line-height: 30px;
  }
  .cta-button {
    position: absolute;
    left: 502px;
    top: 490px;
    width: 220px;
    height: 57px;
    border: 1.5px solid var(--white);
    display: flex;
    align-items: center;
    justify-content: center;
    font-family: 'Montserrat', sans-serif;
    font-weight: 700;
    font-size: 15.5px;
    color: var(--white);
    text-decoration: none;
    text-transform: uppercase;
  }
</style>
</head>
<body>
  <section class="hero">
    <div class="hero-photo" role="img" aria-label="Evening view of a modern residence: glass-walled dining room with chandelier beside a reflecting pool, stepping-stone path and lit hedge of trees"></div>
    <div class="hero-tint"></div>

    <header class="site-header">
      <a class="brand" href="#"><span class="brand-mark"></span>Nexa Holdings</a>
      <nav class="main-nav">
        <a class="nav-home" href="#">Home</a>
        <a class="nav-about" href="#">About</a>
        <a class="nav-strategy" href="#">Strategy</a>
        <a class="nav-project" href="#">Project</a>
        <a class="nav-contact" href="#">Contact</a>
      </nav>
    </header>

    <div class="hero-content">
      <h1 class="hero-title">Private Commercial Real Estate<br>Investment and Development Firm</h1>
      <p class="hero-tagline">Building together. Growing Together.</p>
    </div>

    <a class="cta-button" href="#">Contact Us</a>
  </section>
</body>
</html>
```